Soft furnishing company selling fabrics, curtains, bedlinen craft & haberdashery

We need 4 x home page banners for our website as follows:
Image 1 - to lead customers to our "New season Fabrics" page,
Image 2 - to lead customers to our Ready Made curtains,
Image 3 - to lead customers to our "Polar Bear Bed linen" page
Image 4 - to lead customers to our "Christmas raft Tutorial" page

Banner needs to be 960px wide x 380px 72dpi and optimised for web. should have a little descriptive text for example "Fabulous Fabric. Prints, plains & weaves, view our range of new season furnishing fabrics to buy by the metre" "Instantly update your home with our range of ready made curtains. Available . "Cosy Night In. Snuggle with this Polar Bear Duvet Set. From €20" "" "Let's Get Crafting for Christmas. Download our free Project and tutoirals here. First 3 images need a "shop now" button

website url www.lintelway.ie

Target Market(s)

Female 25 -45

Industry/Entity Type

It Company

Font styles to use
Serif
Sans Serif

Requirements
Must have
• shop now button on image 1, 2, 3
Should not have
• too much text or clutter

```html
<!DOCTYPE html>
<html lang="en">
<head>
<meta charset="UTF-8">
<title>Ready Made Curtains Banner</title>
<link rel="stylesheet" href="https://fonts.googleapis.com/css2?family=Arimo:wght@400&display=swap">
<style>
  :root {
    --green-deep: #2fae7f;
    --green-mid: #45bb8d;
    --green-light: #5cc79a;
    --green-edge: #26a274;
    --white: #ffffff;
    --orange: #f5862a;
    --photo-dark: #544a55;
    --photo-mid: #6e5a5e;
    --photo-light: #a79e98;
  }
  html, body {
    margin: 0;
    padding: 0;
    width: 1200px;
    height: 475px;
    overflow: hidden;
    background: var(--white);
  }
  .banner {
    position: relative;
    width: 1200px;
    height: 475px;
    overflow: hidden;
    background: var(--white);
    font-family: "Arimo", Arial, sans-serif;
  }
  .banner__photo {
    position: absolute;
    inset: 0;
    clip-path: polygon(822px 0, 1200px 0, 1200px 475px, 650px 475px);
    background: linear-gradient(120deg,
      var(--photo-dark) 55%,
      var(--photo-mid) 78%,
      var(--photo-light) 100%);
  }
  .banner__panel {
    position: absolute;
    inset: 0;
  }
  .banner__copy {
    position: absolute;
    left: 68px;
    top: 150px;
    width: 526px;
    margin: 0;
    color: var(--white);
    font-size: 33px;
    line-height: 47px;
    font-weight: 400;
    text-align: center;
  }
  .banner__button {
    position: absolute;
    left: 189px;
    top: 372px;
    width: 272px;
    height: 78px;
    border-radius: 10px;
    background: var(--orange);
    color: var(--white);
    font-size: 33px;
    line-height: 78px;
    text-align: center;
    text-decoration: none;
  }
</style>
</head>
<body>
  <div class="banner">
    <div class="banner__photo" role="img" aria-label="Living room with grey and red tartan eyelet curtains, a leather armchair and a white lamp"></div>

    <svg class="banner__panel" width="1200" height="475" viewBox="0 0 1200 475" aria-hidden="true">
      <defs>
        <linearGradient id="panelGreen" x1="0" y1="0" x2="1" y2="1">
          <stop offset="0" stop-color="#2fae7f"/>
          <stop offset="0.5" stop-color="#45bb8d"/>
          <stop offset="1" stop-color="#5cc79a"/>
        </linearGradient>
      </defs>
      <polygon points="0,0 810,0 638,475 0,475" fill="url(#panelGreen)"/>
      <rect x="0" y="0" width="810" height="3" fill="#26a274"/>
    </svg>

    <p class="banner__copy">Instantly update your home with our range of ready made curtains</p>
    <a class="banner__button" href="#">Shop Now</a>
  </div>
</body>
</html>
```